BrXpertz Business Cards for SME Experts

We need a business card for a new company based in Clearwater FL called Kestrel of Merit. KoM is your access to on-demand subject matter experts. The final design should be very clean communicating innovation and expertise. Our logo design is attached.

The Information Age has affected the workforce in that automation and computerization have resulted in higher productivity coupled with net job loss of many knowledgeable employees. Combined with the creation of the internet and search capabilities, the disintermediation of the value chain of Subject Matter Experts (SME) has happened. We no longer need to work through traditional consulting firms for all consulting needs, instead the direct access to the SME, through a leaner and lower cost model is what the market is demanding.
BrXpertz is a new marketplace to buy consulting services. The business model is that all consultants (subject matter experts) can become a consulting resource in the marketplace following our guidelines. The consumer can now easily access consultants that they could not find easily before.
In much the way an Zyla car can be identified and requested, so can a BrXpertz Consultant. Each consultant can be identified by: location, expertise, billing rate, and prior experience rating.
By seamlessly connecting consultants to requesters through a new Kestrel of Merit marketplace, you now will have an easy to use and quicker turnaround to request and staff your consulting needs. Leveraging the KoM app, you can access the subject matter expert you need for your business requirement.

Target Market(s)

Small and medium sized companies; non-profits

Industry/Entity Type

Business Consultant

Contact Information for Business Card

Name
website
email address
Logo
mailing address (debating if I really need...)
twitter
LinkedIn

Requirements
Must have
• the logo I have included in the design; want the colors to be consistent with the logo design

```html
<!DOCTYPE html>
<html lang="en">
<head>
<meta charset="utf-8">
<title>Kestrel of Merit – Business Card</title>
<link href="https://fonts.googleapis.com/css2?family=Lato:wght@300;400;700&display=swap" rel="stylesheet">
<style>
  :root {
    --backdrop: #d9dadb;
    --card: #fbfbfa;
    --navy: #1f2a6b;
    --cyan: #2ba7d9;
    --ink: #3d3d3f;
    --muted: #5a5a5c;
  }
  * { margin: 0; padding: 0; box-sizing: border-box; }
  html, body {
    width: 1200px; height: 926px; overflow: hidden;
    background: var(--backdrop);
    font-family: "Lato", Arial, sans-serif;
  }
  .card {
    position: absolute; left: 170px; top: 213px;
    width: 860px; height: 500px;
    background: var(--card);
    border-radius: 30px;
    box-shadow: 0 10px 30px rgba(0,0,0,0.18);
  }
  .brand {
    position: absolute; left: 0; right: 0; top: 70px;
    display: flex; flex-direction: column; align-items: center;
    padding-left: 120px;
  }
  .brand-mark {
    width: 56px; height: 56px; border-radius: 50%;
    border: 4px solid var(--navy); margin-bottom: 10px;
  }
  .brand-name {
    font-weight: 700; font-size: 21px; color: var(--navy); letter-spacing: 0.3px;
  }
  .person {
    position: absolute; left: 360px; top: 212px;
  }
  .person-name {
    font-size: 32px; letter-spacing: 2px; line-height: 1;
  }
  .person-name .first { font-weight: 300; color: var(--cyan); }
  .person-name .last { font-weight: 700; color: var(--navy); }
  .person-role {
    font-size: 15px; font-weight: 400; color: var(--muted);
    letter-spacing: 1.2px; margin-top: 6px;
  }
  .contact {
    position: absolute; right: 48px; top: 310px;
    font-size: 17px; color: var(--ink); letter-spacing: 0.6px;
    display: flex; flex-direction: column; align-items: flex-end; gap: 10px;
  }
  .contact-row { display: flex; gap: 30px; align-items: center; white-space: nowrap; }
  .label { color: var(--cyan); font-weight: 700; margin-right: 6px; }
  .social-dot {
    display: inline-block; width: 12px; height: 12px; border-radius: 50%;
    background: var(--cyan); margin-right: 8px; vertical-align: middle;
  }
  .address { text-transform: uppercase; font-size: 16.5px; }
</style>
</head>
<body>
  <div class="card">
    <div class="brand">
      <div class="brand-mark"></div>
      <div class="brand-name">Kestrel of Merit</div>
    </div>

    <div class="person">
      <div class="person-name"><span class="first">JOHN</span> <span class="last">SMITH</span></div>
      <div class="person-role">BUSINESS CONSULTANT</div>
    </div>

    <div class="contact">
      <div class="contact-row address">Street Address Goes Here, Suite #303, Alt Bldg, NY 82365</div>
      <div class="contact-row">
        <span><span class="label">W:</span>www.yourdomain.com</span>
        <span><span class="label">E:</span>yourname@domain.com</span>
      </div>
      <div class="contact-row">
        <span><span class="label">P:</span>123-456-7890</span>
        <span><span class="social-dot"></span>twittername</span>
        <span><span class="social-dot"></span>linkedInname</span>
      </div>
    </div>
  </div>
</body>
</html>
```